Criação de Logo e Rótulo para Consultoria de Negócios
" Temos florestas plantandas de pinus e eucaliptos proprias, de onde extraimos madeira (toras) e subprodutos (por exemplo o mel). Alem disso, os socios prestam serviços de consultoria de gestao, no mesmo CNPJ "

```html
<!DOCTYPE html>
<html lang="pt-BR">
<head>
<meta charset="UTF-8">
<title>Rótulo Mel Flores Silvestres</title>
<link rel="stylesheet" href="https://fonts.googleapis.com/css2?family=Roboto+Condensed:wght@400;700&family=Oswald:wght@500&display=swap">
<style>
  :root {
    --page: #eeeae4;
    --label: #ffffff;
    --gold: #e8b21a;
    --gold-deep: #d49a0c;
    --gold-light: #f6d75e;
    --brown: #4a3210;
    --ink: #222222;
    --grey: #c9c9c9;
    --muted: #7a7a7a;
  }
  * { margin: 0; padding: 0; box-sizing: border-box; }
  html, body { width: 1200px; height: 1200px; overflow: hidden; }
  body {
    background: var(--page);
    font-family: "Roboto Condensed", Arial, sans-serif;
    color: var(--ink);
    position: relative;
  }
  .label {
    position: absolute;
    left: 0; top: 275px;
    width: 1200px; height: 650px;
    background: var(--label);
    border-top: 6px solid var(--gold);
    overflow: hidden;
  }
  .inspection-seal {
    position: absolute; left: 60px; top: 40px;
    width: 170px; height: 170px; border-radius: 50%;
    border: 5px solid var(--grey);
  }
  .date-box {
    position: absolute; left: 112px; top: 240px;
    width: 170px; height: 150px;
  }
  .date-box svg { position: absolute; inset: 0; }
  .date-box .date-title {
    position: absolute; top: 42px; width: 100%;
    text-align: center; font-size: 15px; font-weight: 700;
  }
  .brand {
    position: absolute; left: 0; width: 1200px; top: 95px;
    text-align: center;
    font-size: 74px; font-weight: 700; color: var(--gold-deep);
  }
  .purity-badge {
    position: absolute; left: 790px; top: 35px;
    width: 90px; height: 90px; border-radius: 50%;
    background: radial-gradient(circle, #ffffff 55%, #d9d9d9 100%);
    border: 3px solid #d8d8d8;
    display: flex; flex-direction: column; align-items: center; justify-content: center;
    color: var(--gold-deep); font-weight: 700; line-height: 1;
  }
  .purity-badge .pct { font-size: 22px; }
  .purity-badge .word { font-size: 16px; }
  .storage-notes {
    position: absolute; left: 890px; top: 160px; width: 300px;
    font-size: 15px; line-height: 1.35; color: var(--ink);
  }
  .product {
    position: absolute; left: 0; width: 1200px; top: 285px;
    text-align: center;
  }
  .product .kind { font-size: 28px; font-weight: 700; }
  .product .name {
    font-family: "Oswald", "Arial Narrow", sans-serif;
    font-weight: 500; font-size: 96px; line-height: 1; color: var(--gold);
  }
  .product .variety { font-size: 30px; margin-top: 4px; }
  .honey-band {
    position: absolute; left: 0; bottom: 0; width: 1200px; height: 195px;
    background: linear-gradient(180deg, var(--gold-light) 0%, var(--gold) 55%, var(--gold-deep) 100%);
  }
  .honeycomb-texture {
    position: absolute; left: 300px; top: 0; width: 600px; height: 195px;
    background: linear-gradient(90deg, rgba(255,255,255,0) 0%, rgba(255,240,180,0.35) 50%, rgba(255,255,255,0) 100%);
  }
  .claim {
    position: absolute; left: 150px; top: 28px;
    font-size: 46px; line-height: 1.15; color: var(--brown);
  }
  .net-weight {
    position: absolute; right: 230px; top: 28px;
    font-size: 46px; line-height: 1.15; color: var(--brown); text-align: right;
  }
  .honey-pot {
    position: absolute; right: 20px; bottom: 25px;
    width: 190px; height: 215px; border-radius: 40px 40px 30px 30px;
    background: radial-gradient(circle at 50% 35%, #fff6dc 0%, #f2c24a 55%, #c5810d 100%);
  }
</style>
</head>
<body>
  <section class="label">
    <div class="inspection-seal"></div>

    <div class="date-box">
      <svg viewBox="0 0 170 150" width="170" height="150">
        <polygon points="42,4 128,4 168,75 128,146 42,146 2,75" fill="#ffffff" stroke="#e8b21a" stroke-width="3"/>
      </svg>
      <div class="date-title">Data de fabricação:</div>
    </div>

    <div class="brand">Bosque Doce</div>

    <div class="purity-badge"><span class="pct">100%</span><span class="word">PURO</span></div>

    <p class="storage-notes">Conservar em local seco e arejado.<br>A cristalização pode ocorrer, pois trata-se de um produto PURO.<br>Colocar em banho maria (até 45ºC) para voltar ao seu estado líquido.</p>

    <div class="product">
      <div class="kind">Produto Orgânico</div>
      <div class="name">Mel</div>
      <div class="variety">Flores Silvestres</div>
    </div>

    <div class="honey-band">
      <div class="honeycomb-texture" role="img" aria-label="Textura de favo de mel em tons dourados"></div>
      <div class="claim">Sem<br>Conservantes</div>
      <div class="net-weight">Peso Líquido<br>300g</div>
    </div>
    <div class="honey-pot" role="img" aria-label="Ilustração de pote de mel com colher escorrendo mel"></div>
  </section>
</body>
</html>
```